Service Plan Sales Flyer

The Watchpost Depot (www.kelvamart.com) is a commercial security integrator that installs security cameras, access control, intrusion, two-way radios and perimeter security. We require a one page flyer for our service plan for new and existing customers. The price of the service plan is $299/yr and includes the following;
1. Discounted service rate of $118/hr
2. Free remote support ($85/hr without a plan)
3. Free remote training
4. Priority support

Please review our brochure attached and create a one page sales flyer with the end goal of having the client sign up for our annual service plan . The plan will automatically renew every year. Email sales@kelvamart.com.

Target Market(s)

commercial industrial clients - no residential

Industry/Entity Type

review our website at www.kelvamart.com

Colors
0054AA
0677BA
7BADD7
CADEEF
E8F1F8
EE7325
F08F49
F5BC92
FAE3D3
FDF4ED

Requirements
Must have
• call to action
Should not have
• too many colors

```html
<!DOCTYPE html>
<html lang="en">
<head>
<meta charset="utf-8">
<title>The Watchpost Depot — Service Plan Flyer</title>
<link rel="stylesheet" href="https://fonts.googleapis.com/css2?family=Oswald:wght@500;600;700&family=Poppins:wght@400;600&display=swap">
<style>
  :root {
    --page-bg: #5c5c5c;
    --navy: #0d2f63;
    --blue-deep: #2f68c2;
    --blue-mid: #5a8fdc;
    --blue-light: #b9cff0;
    --panel: #e8f1f8;
    --red: #e8392f;
    --icon-blue: #4f86cf;
    --ink: #1d2230;
    --white: #ffffff;
  }
  * { box-sizing: border-box; margin: 0; padding: 0; }
  html, body { width: 1200px; height: 1200px; overflow: hidden; background: var(--page-bg); }
  .stage { position: relative; width: 1200px; height: 1200px; }
  .flyer {
    position: absolute; left: 150px; top: 18px;
    width: 858px; height: 1109px;
    transform: scale(1.05); transform-origin: top left;
    background: var(--white); overflow: hidden;
    font-family: "Poppins", sans-serif; color: var(--ink);
  }
  .hero {
    position: absolute; left: 0; top: 0; width: 858px; height: 640px;
    background: linear-gradient(180deg, #d3def5 0%, #9dbbea 35%, #5f92dc 70%, #3a74c9 100%);
  }
  .hero-photo {
    position: absolute; left: 250px; top: 95px; width: 608px; height: 510px;
    background: radial-gradient(circle at 52% 45%, #3fa9b8 0%, #2a5f8f 22%, #cfd9ea 42%, rgba(180,200,235,0.4) 70%, rgba(150,180,230,0) 100%);
  }
  .brand { position: absolute; left: 30px; top: 24px; display: flex; align-items: center; gap: 16px; }
  .brand-square { width: 44px; height: 44px; background: var(--navy); }
  .brand-name { font-family: "Oswald", sans-serif; font-weight: 700; font-size: 34px; letter-spacing: 1px; color: var(--navy); text-transform: uppercase; line-height: 1; }
  .brand-tag { position: absolute; left: 90px; top: 78px; font-family: "Oswald", sans-serif; font-weight: 500; font-size: 11px; color: var(--navy); }
  .echo { position: absolute; left: 8px; top: 135px; font-family: "Oswald", sans-serif; font-weight: 700; font-size: 58px; line-height: 62px; color: rgba(255,255,255,0.3); }
  .headline { position: absolute; left: 25px; top: 428px; font-family: "Oswald", sans-serif; font-weight: 600; text-transform: uppercase; line-height: 1; }
  .headline .kicker { font-size: 29px; color: var(--navy); }
  .headline .line { font-size: 40px; color: var(--white); margin-top: 8px; }
  .headline .big { font-size: 72px; color: var(--white); font-weight: 700; margin-top: 2px; }
  .slant { position: absolute; left: 0; top: 570px; }
  .lower-bg { position: absolute; left: 0; top: 600px; width: 858px; height: 470px; background: #f3f5f9; z-index: -1; }
  .plan-panel { position: absolute; left: 22px; top: 596px; width: 431px; height: 469px; background: var(--panel); padding: 26px 30px 0 30px; }
  .plan-title { font-size: 22px; color: var(--ink); }
  .plan-price { font-family: "Oswald", sans-serif; font-weight: 700; font-size: 62px; color: var(--red); line-height: 1.05; letter-spacing: -0.5px; }
  .plan-note { text-align: right; font-size: 16px; color: #555c6a; margin-right: 24px; }
  .benefits { list-style: none; margin-top: 22px; }
  .benefit { display: flex; align-items: center; gap: 16px; height: 70px; border-bottom: 1px solid #d3dde9; font-size: 17px; line-height: 1.2; color: var(--ink); }
  .benefit:last-child { border-bottom: none; }
  .benefit strong { font-weight: 600; color: var(--navy); }
  .benefit svg { flex: none; width: 46px; height: 46px; }
  .product-shot {
    position: absolute; left: 380px; top: 645px; width: 460px; height: 400px;
    background: radial-gradient(ellipse at 60% 45%, #c9d3e0 0%, #e8ecf2 55%, rgba(243,245,249,0) 80%);
  }
  .footer { position: absolute; left: 0; top: 1072px; width: 858px; display: flex; justify-content: space-between; padding: 0 50px 0 27px; font-size: 15px; letter-spacing: 0.5px; color: var(--ink); }
  .footer span { display: flex; align-items: center; gap: 9px; }
  .footer svg { width: 16px; height: 16px; }
</style>
</head>
<body>
<div class="stage">
  <div class="flyer">
    <div class="lower-bg"></div>
    <section class="hero">
      <div class="hero-photo" role="img" aria-label="Close-up photograph of a bullet security camera with infrared LEDs"></div>
      <div class="brand">
        <div class="brand-square"></div>
        <div class="brand-name">The Watchpost Depot</div>
      </div>
      <div class="brand-tag">Commercial &amp; Industrial Solutions</div>
      <div class="echo" aria-hidden="true">SECURITY+<br>SECURITY+<br>SECURITY+<br>SECURITY+</div>
      <div class="headline">
        <div class="kicker">Canada's Most Trusted</div>
        <div class="line">Commercial Security</div>
        <div class="big">Integrator</div>
      </div>
    </section>

    <svg class="slant" width="858" height="80" viewBox="0 0 858 80">
      <polygon points="0,67 858,15 858,30 0,82" fill="var(--red)"/>
      <polygon points="0,82 858,30 858,80 0,80" fill="#f3f5f9"/>
    </svg>

    <div class="product-shot" role="img" aria-label="Product photos: video management software on a monitor, a dome camera, a bullet camera and a shield icon"></div>

    <section class="plan-panel">
      <h2 class="plan-title" style="font-weight:400">Our Service Plan</h2>
      <div class="plan-price">$299/YR ONLY</div>
      <p class="plan-note">*and includes the following</p>
      <ul class="benefits">
        <li class="benefit">
          <svg viewBox="0 0 46 46"><path d="M23 3l5 4 6-1 2 6 6 3-1 6 4 5-4 5 1 6-6 3-2 6-6-1-5 4-5-4-6 1-2-6-6-3 1-6-4-5 4-5-1-6 6-3 2-6 6 1z" fill="var(--icon-blue)"/><circle cx="17" cy="17" r="3.5" fill="#fff"/><circle cx="29" cy="29" r="3.5" fill="#fff"/><line x1="30" y1="15" x2="16" y2="31" stroke="#fff" stroke-width="3"/></svg>
          <span>Discounted service<br>rate of <strong>$118/hr</strong></span>
        </li>
        <li class="benefit">
          <svg viewBox="0 0 46 46"><path d="M8 24a15 15 0 0 1 30 0" fill="none" stroke="var(--icon-blue)" stroke-width="3"/><rect x="4" y="22" width="7" height="12" rx="3" fill="var(--icon-blue)"/><rect x="35" y="22" width="7" height="12" rx="3" fill="var(--icon-blue)"/><ellipse cx="23" cy="27" rx="11" ry="8" fill="var(--icon-blue)"/><circle cx="18" cy="27" r="1.8" fill="#fff"/><circle cx="23" cy="27" r="1.8" fill="#fff"/><circle cx="28" cy="27" r="1.8" fill="#fff"/></svg>
          <span>Free remote support<br>(<strong>$85/hr</strong> without a plan)</span>
        </li>
        <li class="benefit">
          <svg viewBox="0 0 46 46"><circle cx="11" cy="12" r="5" fill="var(--icon-blue)"/><path d="M4 42V24a6 6 0 0 1 12 0v18z" fill="var(--icon-blue)"/><rect x="18" y="8" width="24" height="18" fill="none" stroke="var(--icon-blue)" stroke-width="2.5"/><line x1="22" y1="14" x2="38" y2="14" stroke="var(--icon-blue)" stroke-width="2"/><line x1="22" y1="20" x2="34" y2="20" stroke="var(--icon-blue)" stroke-width="2"/><line x1="30" y1="26" x2="26" y2="40" stroke="var(--icon-blue)" stroke-width="2"/><line x1="30" y1="26" x2="34" y2="40" stroke="var(--icon-blue)" stroke-width="2"/></svg>
          <span>Free remote<br>training</span>
        </li>
        <li class="benefit">
          <svg viewBox="0 0 46 46"><circle cx="27" cy="9" r="4.5" fill="var(--icon-blue)"/><rect x="20" y="15" width="14" height="10" rx="3" fill="var(--icon-blue)"/><path d="M3 40l9-10h10l8 4 10-6 3 3-12 10H16l-7 4z" fill="var(--icon-blue)"/></svg>
          <span>Priority<br>support</span>
        </li>
      </ul>
    </section>

    <footer class="footer">
      <span><svg viewBox="0 0 16 16"><circle cx="8" cy="8" r="7" fill="none" stroke="#1d2230" stroke-width="1.5"/><ellipse cx="8" cy="8" rx="3" ry="7" fill="none" stroke="#1d2230" stroke-width="1.3"/><line x1="1" y1="8" x2="15" y2="8" stroke="#1d2230" stroke-width="1.3"/></svg>www.kelvamart.com</span>
      <span><svg viewBox="0 0 16 16"><rect x="1" y="3" width="14" height="10" fill="#1d2230"/><path d="M1 3l7 6 7-6" fill="none" stroke="#fff" stroke-width="1.3"/></svg>sales@kelvamart.com</span>
      <span><svg viewBox="0 0 16 16"><path d="M3 1l3 3-1.5 2.5a9 9 0 0 0 5 5L12 10l3 3-2 2.5C7 15 1 9 .5 3z" fill="#1d2230"/></svg>1-877-555-0148</span>
    </footer>
  </div>
</div>
</body>
</html>
```